I'd like a business card that makes my company, Fenwright Marsh Associates Ltd stand out from the normal financial & IT services sector . It would be great to have a card that a potential client will think "wow" this is out of the norm , I'll give these guys a call. My business aims to provide consultancy services for financial and IT institutions but I'm looking to provide a newer approach that fits into today's social media rather than the standard "big 4" approach. My business helps companies assess their internal issues and aims to solve issues via business process re-engineering. The final design should have a balance of the maturity of the financial & IT sector with the fresh approach of the thriving social media sector

Target Market(s)

Business Managers and Directors, technical Managers and directors. Aged between 20 and 60 that handle project budgets

Industry/Entity Type

Financial

Requirements
Must have
• Must incorporate company logo currently being designed
Should not have
• No old-style fonts please.

```html
<!DOCTYPE html>
<html lang="en">
<head>
<meta charset="utf-8">
<title>Fenwright Marsh Associates Ltd — Business Card</title>
<link rel="stylesheet" href="https://fonts.googleapis.com/css2?family=Montserrat:wght@500;600;700&family=Open+Sans:wght@400;600&display=swap">
<style>
  :root {
    --backdrop: #e9e6e2;
    --orange-deep: #c4530f;
    --orange-mid: #dc6a1c;
    --orange-glow: #f08a3a;
    --plum: #9c1f6a;
    --ink: #4a4a4a;
    --ink-soft: #666666;
    --paper: #ffffff;
    --white: #ffffff;
  }
  * { box-sizing: border-box; margin: 0; padding: 0; }
  html, body {
    width: 1200px; height: 900px; overflow: hidden;
    background: var(--backdrop);
  }
  .canvas {
    position: relative; width: 1200px; height: 900px;
    display: flex; flex-direction: column; align-items: center; justify-content: center; gap: 40px;
  }
  .card {
    position: relative; width: 700px; height: 400px;
    box-shadow: 0 10px 28px rgba(0,0,0,0.18);
    overflow: hidden;
  }

  /* Front (orange) */
  .card--front {
    background:
      radial-gradient(circle at 55% 45%, var(--orange-glow) 0%, var(--orange-mid) 38%, var(--orange-deep) 85%);
  }
  .card--front .band {
    position: absolute; top: 0; bottom: 0; left: 95px; width: 150px;
    background: rgba(255,255,255,0.06);
    border-left: 1px solid rgba(255,255,255,0.08);
    border-right: 1px solid rgba(255,255,255,0.08);
  }
  .card--front .wordmark {
    position: absolute; right: 48px; top: 205px; text-align: center;
    font-family: "Montserrat", sans-serif; font-weight: 700; color: var(--white);
  }
  .wordmark .wordmark__name { font-size: 26px; letter-spacing: 0.5px; line-height: 1.1; }
  .wordmark .wordmark__suffix { font-size: 14px; letter-spacing: 3px; margin-top: 4px; }

  /* Back (white) */
  .card--back { background: var(--paper); }
  .brand {
    position: absolute; left: 40px; top: 95px; width: 320px;
    display: flex; flex-direction: column; align-items: center;
    font-family: "Montserrat", sans-serif; font-weight: 700; color: var(--ink);
  }
  .brand__square {
    width: 110px; height: 110px; background: var(--orange-mid); margin-bottom: 22px;
  }
  .brand .wordmark__name { font-size: 27px; letter-spacing: 0.5px; text-align: center; line-height: 1.15; }
  .brand .wordmark__suffix { font-size: 15px; letter-spacing: 4px; margin-top: 4px; }

  .divider {
    position: absolute; left: 378px; top: 120px; width: 3px; height: 150px;
    background: linear-gradient(to bottom, rgba(220,106,28,0), var(--orange-mid) 50%, rgba(220,106,28,0));
  }

  .contact {
    position: absolute; left: 405px; top: 78px; right: 30px;
    font-family: "Open Sans", sans-serif; color: var(--ink);
  }
  .contact__name {
    font-family: "Montserrat", sans-serif; font-weight: 700; font-size: 25px; color: var(--plum); line-height: 1.1;
  }
  .contact__role { font-size: 14px; color: var(--ink-soft); margin-bottom: 16px; }
  .contact__address { font-size: 14px; line-height: 1.45; margin-bottom: 14px; }
  .contact__list { list-style: none; }
  .contact__item { display: flex; align-items: center; gap: 10px; font-size: 15px; line-height: 1.55; }
  .contact__item svg { width: 13px; height: 13px; fill: var(--plum); flex: none; }
</style>
</head>
<body>
<main class="canvas">

  <section class="card card--front" aria-label="Card front">
    <div class="band"></div>
    <div class="wordmark">
      <div class="wordmark__name">FENWRIGHT MARSH</div>
      <div class="wordmark__suffix">Associates Ltd</div>
    </div>
  </section>

  <section class="card card--back" aria-label="Card back">
    <div class="brand">
      <div class="brand__square"></div>
      <div class="wordmark__name">FENWRIGHT MARSH</div>
      <div class="wordmark__suffix">Associates Ltd</div>
    </div>

    <div class="divider"></div>

    <div class="contact">
      <div class="contact__name">Dorian Keswick</div>
      <div class="contact__role">Managing Member</div>
      <div class="contact__address">2217 Harbor Crest Drive,<br>Fresno, CA 93711</div>
      <ul class="contact__list">
        <li class="contact__item">
          <svg viewBox="0 0 16 16" aria-hidden="true"><path d="M3.5 1l2.5 3-1.5 1.8c.9 2 2.7 3.8 4.7 4.7L11 9l3 2.5-1.3 2.8C7 14 2 9 1.7 2.3z"/></svg>
          (559) 408-2713
        </li>
        <li class="contact__item">
          <svg viewBox="0 0 16 16" aria-hidden="true"><rect x="4" y="1" width="8" height="4"/><rect x="1" y="6" width="14" height="6" rx="1"/><rect x="4" y="10" width="8" height="5"/></svg>
          (559) 408-2714
        </li>
        <li class="contact__item">
          <svg viewBox="0 0 16 16" aria-hidden="true"><path d="M4 0h8a1 1 0 0 1 1 1v14a1 1 0 0 1-1 1H4a1 1 0 0 1-1-1V1a1 1 0 0 1 1-1zm1 2v10h6V2z"/></svg>
          (559) 731-5820
        </li>
        <li class="contact__item">
          <svg viewBox="0 0 16 16" aria-hidden="true"><path d="M1 3h14v1.2L8 9 1 4.2z"/><path d="M1 5.6l7 4.8 7-4.8V13H1z"/></svg>
          dorian@fenwrightmarsh.com
        </li>
        <li class="contact__item">
          <svg viewBox="0 0 16 16" aria-hidden="true"><circle cx="8" cy="8" r="7" fill="none" stroke="#9c1f6a" stroke-width="1.6"/><path d="M1 8h14M8 1c-3 3.5-3 10.5 0 14M8 1c3 3.5 3 10.5 0 14" fill="none" stroke="#9c1f6a" stroke-width="1.4"/></svg>
          www.fenwrightmarsh.com
        </li>
      </ul>
    </div>
  </section>

</main>
</body>
</html>
```